Corporate Design für eine Veranstaltungsagentur
Vielen Dank an Bartholdt, der trotz vieler unserer Revisionswünsche stets freundlich war, professionell und schnell gearbeitet hat und uns am Ende ein wirklich wunderbares Ergebnis geliefert hat! :-) Wir können ihn uneingeschränkt weiterempfehlen!
Zielgruppe
Agentur zur Planung, Organisation und Durchführung von Veranstaltungen aller Art
Ingenieurbetrieb für Veranstaltungstechnik und - produktion
Organisation und Durchführung der 'Nebelklang'-Veranstaltungsreihe: www.nebelklang-turnier.de
Zielgruppe:
Personen jeder Altersgruppe, Privatpersonen, Geschäftskunden
Aufgabenstellung
Die Farbe Grün sollte beibehalten werden.
Logo soll Professionalität und Innovation ausstrahlen, gleichzeitig modern und zeitlos wirken.

```html
<!DOCTYPE html>
<html lang="de">
<head>
<meta charset="utf-8">
<title>Lumivo Events – Geschäftsausstattung</title>
<link href="https://fonts.googleapis.com/css2?family=Ubuntu:wght@400;500;700&display=swap" rel="stylesheet">
<style>
  :root{
    --stage:#2e2f31;
    --paper:#ffffff;
    --ink:#2b2b2b;
    --green:#8cc63f;
    --green-dark:#3ea043;
    --card-dark:#3b3c3a;
    --rule:#bdbdbd;
    --ghost:#f3f3f3;
  }
  *{margin:0;padding:0;box-sizing:border-box}
  html,body{width:1200px;height:856px;overflow:hidden;background:var(--stage)}
  body{position:relative;font-family:"Ubuntu",sans-serif;color:var(--ink)}

  .letterhead{position:absolute;left:139px;top:134px;width:416px;height:588px;background:var(--paper);overflow:hidden}
  .letterhead__ghost{position:absolute;left:45px;top:200px;width:190px;height:190px;border-radius:50%;background:var(--ghost)}
  .brand{display:flex;align-items:center;gap:4px;font-weight:500;color:var(--green-dark);line-height:1;white-space:nowrap}
  .brand__dot{border-radius:50%;background:var(--green);flex:none}
  .letterhead .brand{position:absolute;right:40px;top:44px;font-size:11px}
  .letterhead .brand__dot{width:9px;height:9px}
  .sender-line{position:absolute;left:45px;top:92px;font-size:4px;color:var(--green);border-bottom:0.5px solid var(--green);padding-bottom:1px;white-space:nowrap}
  .recipient{position:absolute;left:45px;top:109px;font-size:6px;line-height:8.4px}
  .recipient .city{margin-top:8px}
  .subject{position:absolute;left:45px;top:201px;font-size:6px;font-weight:700}
  .body-copy{position:absolute;left:45px;top:224px;width:226px;font-size:5.9px;line-height:7.65px;text-align:left}
  .body-copy p+p{margin-top:7px}
  .closing{position:absolute;left:45px;top:421px;font-size:5.4px}
  .signature{position:absolute;left:45px;top:439px;width:88px;height:16px;background:var(--ink);opacity:.85;border-radius:2px}
  .letter-footer{position:absolute;left:84px;top:543px;width:249px;border-top:0.8px solid var(--green);display:flex;justify-content:space-between;padding-top:6px}
  .letter-footer div{font-size:3.6px;line-height:5px;text-align:center;font-weight:500;width:80px;white-space:nowrap}

  .card{position:absolute;top:291px;width:163px;height:252px;overflow:hidden}
  .card--front{left:665px;background:var(--paper)}
  .card--back{left:898px;background:var(--card-dark);display:flex;align-items:center;justify-content:center}
  .card__ghost{position:absolute;left:30px;top:120px;width:140px;height:120px;border-radius:50%;background:var(--ghost)}
  .card--front .brand{position:absolute;left:0;right:0;top:52px;justify-content:center;font-size:14px}
  .card--front .brand__dot{width:11px;height:11px}
  .card__rule{position:absolute;left:25px;top:113px;width:112px;height:1px;background:var(--rule)}
  .card__details{position:absolute;left:0;right:0;top:135px;text-align:center;font-size:6.8px;line-height:9.4px}
  .card__name{font-weight:500}
  .card__role{color:var(--green)}
  .card__gap{height:5px}
  .card__web{color:var(--green-dark);font-weight:700;margin-top:5px}
  .card--back .brand{color:var(--green);font-size:15px}
  .card--back .brand__dot{width:12px;height:12px}
</style>
</head>
<body>
  <section class="letterhead">
    <div class="letterhead__ghost" aria-hidden="true"></div>
    <div class="brand"><span class="brand__dot"></span>Lumivo Events</div>
    <div class="sender-line">Vorname Nachname, Lindenweg 7, 54321 Talheim</div>
    <div class="recipient">
      <div>Jana Beispiel</div>
      <div>Ahornallee 18</div>
      <div class="city">10115 Berlin</div>
    </div>
    <div class="subject">Quidero molore, atatur sae. Nequat,</div>
    <div class="body-copy">
      <p>Ur sit, imus, ipicatem voluptate eum re dolluptios sequosam, eum reritati am volor sapedissi quo blaboribust, sequass itasped igendi cus exerfer feruptas iusanda ndaest, qui omnis nus aut fugitinis quatur ad ullaut mostem quasperiae corem et aciatem illatin ciduntores quidis utemquam autemperae soluptiae lab illacescia solorum et fugiam ratatatus exerro blaciis samusam etur? Uga. Neque nam simi, nest, ommod essedios magnatia nossi aute nonsequam fugiaspis moluptas sed el int etur saepe nonsecatem excea noneceperrum ulligendit faccullores et lantur si ium at.Ota cuptae non ea de opta voles rem rae dolore ilia vellab isi blanis idit veribus auda alit labore desenis imenis que in con rehent, explat ped que volorum, autent, si tetur?</p>
      <p>Ihil ium restior ecepero reptistius es aborepe diatiunt dignis diciae voluptu ribearit, que nat aute et as maximus, qui blab iur aut volest, nonsequae odios doluptatiae velignimin perescia vent. Pa voluptas expero corectur molest eaquid enda vidus verciis quodi te dit aliquid unturem poreper feratur? Quis aut rehenihilit et quam, eris et perorru mquamusa quo et untia volupie nisimoluptae esseribus cora doluptati doluptatur atisciumqui re pa quat aut lam solescia intiis et millabor sit odis et quos re sam, vendicientur abo. Equi totatus rest, nosam quodi omni doloriosam des ea nimpelique volo elendae dellign ihilitis solupta temporp orupta iuntia ipiste natibusapis volesedis reriori taerrup tatiberes nobitiur, sequi omnihillab id maximagnat omnimus dolo quunt, int aut earum lacit peliquunt iduciet, id que autemolum deruptati te non re.</p>
    </div>
    <div class="closing">Sincerely</div>
    <div class="signature" role="img" aria-label="Handschriftliche Unterschrift"></div>
    <footer class="letter-footer">
      <div>Lumivo Events GmbH<br>Lindenweg 7<br>54321 Talheim</div>
      <div>T: 030 / 987 650 12<br>F: 030 / 987 650 13<br>info@beispielnetz.de</div>
      <div>Haldenbank ag<br>IBAN: DE98 7654 3210 0088<br>BIC: HALDEBB1XXX</div>
    </footer>
  </section>

  <section class="card card--front">
    <div class="card__ghost" aria-hidden="true"></div>
    <div class="brand"><span class="brand__dot"></span>Lumivo Events</div>
    <div class="card__rule"></div>
    <div class="card__details">
      <div class="card__name">Vorname Nachname</div>
      <div class="card__role">Geschäftsführung</div>
      <div class="card__gap"></div>
      <div>Lindenweg 7</div>
      <div>54321 Talheim</div>
      <div class="card__gap"></div>
      <div>T: 030 / 987 650 12</div>
      <div>F: 030 / 987 650 13</div>
      <div>info@beispielnetz.de</div>
      <div class="card__web">www.beispielnetz.de</div>
    </div>
  </section>

  <section class="card card--back">
    <div class="brand"><span class="brand__dot"></span>Lumivo Events</div>
  </section>
</body>
</html>
```